BrindleStaffing Business Card Design

We are a staffing company finding positions for dedicated nurses and physicians.

Target Market(s)

Business Professionals

Industry/Entity Type

Staffing

Contact Information for Business Card

Gregory Malden
Chairman
417 39th Crescent South
SAINT PETERSBURG FL 33719
813-555-0147 Mobile
813-555-0183 Fax
gmalden@brindlestaffing.example
www.brindlestaffing.example

Font styles to use
Sans Serif

Colors
fbee3e
f04a50
f37122

Requirements
Must have
• Logo Attached, see colors below. We'd like to see Yellow, Orange and Red.

```html
<!DOCTYPE html>
<html lang="en">
<head>
<meta charset="utf-8">
<title>BrindleStaffing Business Card</title>
<link rel="stylesheet" href="https://fonts.googleapis.com/css2?family=Arimo:wght@400;700&display=swap">
<style>
  :root {
    --backdrop: #e9e7e4;
    --card: #ffffff;
    --card-shade: #f2f2f2;
    --brand-yellow: #fbee3e;
    --brand-red: #f04a50;
    --brand-orange: #f37122;
    --ink: #222222;
    --ink-soft: #444444;
  }
  * { box-sizing: border-box; margin: 0; padding: 0; }
  html, body {
    width: 1200px; height: 800px; overflow: hidden;
    background: var(--backdrop);
    font-family: "Arimo", Arial, sans-serif;
    color: var(--ink);
  }
  .canvas {
    position: relative; width: 1200px; height: 800px;
    display: flex; align-items: center; justify-content: center; gap: 60px;
  }
  .card {
    position: relative; width: 500px; height: 286px;
    background: linear-gradient(160deg, var(--card) 40%, var(--card-shade));
    box-shadow: 0 10px 28px rgba(0,0,0,0.18);
    overflow: hidden;
  }
  .card-edge {
    position: absolute; left: 0; right: 0; bottom: 0;
    height: 10px; background: var(--brand-orange);
  }
  .brand {
    display: flex; align-items: center; white-space: nowrap;
  }
  .brand-dot {
    flex: none; border-radius: 50%; background: var(--brand-yellow);
  }
  .brand-name {
    font-weight: 700; color: var(--brand-red); letter-spacing: -0.5px;
  }
  .card-front { display: flex; align-items: center; justify-content: center; }
  .card-front .brand { gap: 12px; margin-bottom: 10px; }
  .card-front .brand-dot { width: 30px; height: 30px; }
  .card-front .brand-name { font-size: 42px; }
  .card-back .brand {
    position: absolute; top: 48px; right: 36px; gap: 8px;
  }
  .card-back .brand-dot { width: 16px; height: 16px; }
  .card-back .brand-name { font-size: 24px; }
  .holder { position: absolute; left: 36px; top: 150px; }
  .holder-name { font-size: 17px; font-weight: 400; }
  .holder-title { font-size: 10px; color: var(--ink-soft); margin-top: 2px; }
  .contact-list {
    position: absolute; left: 36px; top: 192px; list-style: none;
    font-size: 9.5px; line-height: 14px; color: var(--ink-soft);
  }
  .contact-list li { display: flex; align-items: center; gap: 7px; }
  .icon { width: 9px; height: 9px; fill: var(--ink); flex: none; }
  .address {
    position: absolute; right: 36px; top: 200px;
    display: flex; gap: 7px; align-items: flex-start;
    font-size: 9px; line-height: 12px; color: var(--ink-soft);
  }
  .address .icon { width: 8px; height: 11px; margin-top: 1px; }
</style>
</head>
<body>
<main class="canvas">
  <section class="card card-front" aria-label="Card front">
    <div class="brand">
      <span class="brand-dot"></span>
      <span class="brand-name">BrindleStaffing</span>
    </div>
    <span class="card-edge"></span>
  </section>

  <section class="card card-back" aria-label="Card back">
    <div class="brand">
      <span class="brand-dot"></span>
      <span class="brand-name">BrindleStaffing</span>
    </div>
    <div class="holder">
      <p class="holder-name">Gregory Malden</p>
      <p class="holder-title">Chairman</p>
    </div>
    <ul class="contact-list">
      <li>
        <svg class="icon" viewBox="0 0 10 10"><path d="M2 0.5 L3.8 2.6 L2.9 3.7 Q4 6 6.3 7.1 L7.4 6.2 L9.5 8 L8.3 9.5 Q3.5 9 0.5 1.7 Z"/></svg>
        813-555-0147 Mobile
      </li>
      <li>
        <svg class="icon" viewBox="0 0 10 10"><rect x="0.5" y="3" width="9" height="6.5" rx="1"/><rect x="2.5" y="0.5" width="5" height="3" fill="none" stroke="#222" stroke-width="1"/></svg>
        813-555-0183 Fax
      </li>
      <li>
        <svg class="icon" viewBox="0 0 10 10"><rect x="0.5" y="1.5" width="9" height="7" fill="none" stroke="#222" stroke-width="1"/><path d="M0.5 1.5 L5 5.5 L9.5 1.5" fill="none" stroke="#222" stroke-width="1"/></svg>
        gmalden@brindlestaffing.example
      </li>
      <li>
        <svg class="icon" viewBox="0 0 10 10"><circle cx="5" cy="5" r="4.5"/><path d="M0.5 5 H9.5 M5 0.5 V9.5 M5 0.5 Q2 5 5 9.5 M5 0.5 Q8 5 5 9.5" fill="none" stroke="#fff" stroke-width="0.7"/></svg>
        www.brindlestaffing.example
      </li>
    </ul>
    <div class="address">
      <svg class="icon" viewBox="0 0 8 11"><path d="M4 0.5 A3.5 3.5 0 0 1 7.5 4 Q7.5 6.5 4 10.5 Q0.5 6.5 0.5 4 A3.5 3.5 0 0 1 4 0.5 Z"/><circle cx="4" cy="4" r="1.3" fill="#fff"/></svg>
      <p>417 39th Crescent South<br>SAINT PETERSBURG FL 33719</p>
    </div>
    <span class="card-edge"></span>
  </section>
</main>
</body>
</html>
```